seeking a modern Business Card design for Roof Plumbering Business

halbury roof plumbing is a local metal re-roof and new construction specialist. We are seeking a modern business card to assist with networking within the industry. Our services are predominantly the installation of metal roofs on new houses, however we also do re-roofs when an existing roof needs replacing. We service both residential and commercial properties. Please include the below details on the card:
Name: Owen Halbury
Phone: 0481 257 936
Email: owenhalburyroofing@tindlemail.com

Residential & Commercial
Re-roof & New Construction
Fully Insured

I have uploaded our business logo, which we think would suit a black background. Please use all lower case for business name.
Cheers
Updates

Hey Guys, As requested I've uploaded a Pdf version of my logo. Hopefully this help. Thanks

Industry/Entity Type

Business

Contact Information for Business Card

Name: Owen Halbury
Phone: 0481 257 936

Residential & Commercial
Fully Insured

Font styles to use
Serif
Sans Serif

Requirements
Must have
• Name must be all lower case "halbury roof plumbing"
Nice to have
• Stick with Logo Colours

```html
<!DOCTYPE html>
<html lang="en">
<head>
<meta charset="utf-8">
<title>halbury roof plumbing – business card</title>
<link href="https://fonts.googleapis.com/css2?family=Montserrat:wght@300;400;500;600&display=swap" rel="stylesheet">
<style>
  :root {
    --cyan: #27b9dd;
    --cyan-light: #3fc6e6;
    --cyan-deep: #1aa6cc;
    --black: #0b0b0c;
    --white: #ffffff;
    --ink: #1d2226;
    --page: #e9e6e1;
  }
  * { box-sizing: border-box; margin: 0; padding: 0; }
  html, body {
    width: 1200px; height: 1022px; overflow: hidden;
    background: var(--page);
    font-family: "Montserrat", Arial, sans-serif;
  }
  .sheet {
    position: relative; width: 1200px; height: 1022px;
  }
  .card {
    position: absolute; left: 190px;
    width: 820px; height: 456px;
    border-radius: 22px; overflow: hidden;
    background: linear-gradient(160deg, var(--cyan-light) 0%, var(--cyan) 55%, var(--cyan-deep) 100%);
    box-shadow: 0 10px 30px rgba(0,0,0,0.18);
  }
  .card--front { top: 35px; }
  .card--back { top: 531px; }

  .band {
    position: absolute; left: 0; right: 0; bottom: 0; height: 160px;
    background: var(--black);
    border-top: 6px solid var(--white);
  }

  /* Front */
  .brand {
    position: absolute; left: 64px; top: 96px;
    display: flex; align-items: center; gap: 18px;
  }
  .brand__mark {
    width: 22px; height: 22px; background: var(--ink);
  }
  .brand__name {
    font-size: 46px; font-weight: 400; color: var(--ink);
    letter-spacing: 1px; line-height: 1;
  }
  .company {
    position: absolute; left: 290px; bottom: 186px;
    font-size: 25px; font-weight: 600; letter-spacing: 2px;
    color: var(--ink); text-transform: uppercase;
  }
  .contact {
    position: absolute; left: 290px; top: 26px;
  }
  .contact__name {
    font-size: 36px; font-weight: 500; letter-spacing: 2px;
    color: var(--cyan); text-transform: uppercase; margin-bottom: 14px;
  }
  .contact__line {
    display: flex; align-items: center; gap: 14px;
    font-size: 22px; font-weight: 400; color: var(--cyan);
    letter-spacing: 0.5px; margin-bottom: 6px;
  }
  .contact__icon { width: 16px; height: 16px; flex: none; }

  /* Back */
  .services {
    position: absolute; right: 54px; top: 22px; text-align: right;
  }
  .services__item {
    font-size: 24px; font-weight: 300; color: var(--cyan);
    letter-spacing: 1.5px; line-height: 1.5;
  }
</style>
</head>
<body>
<main class="sheet">

  <section class="card card--front" aria-label="Business card front">
    <div class="brand">
      <span class="brand__mark"></span>
      <span class="brand__name">halbury roof plumbing</span>
    </div>
    <p class="company">Halbury Roof Plumbing</p>
    <div class="band">
      <div class="contact">
        <p class="contact__name">Owen Halbury</p>
        <p class="contact__line">
          <svg class="contact__icon" viewBox="0 0 16 16" aria-hidden="true">
            <path d="M3 1.5l3 3-1.6 1.8c.9 2 2.3 3.4 4.3 4.3L10.5 9l3 3-1.8 2.2C6.5 14 2 9.5 1.5 4.3z" fill="none" stroke="#27b9dd" stroke-width="1.3" stroke-linejoin="round"/>
          </svg>
          0481 257 936
        </p>
        <p class="contact__line">
          <svg class="contact__icon" viewBox="0 0 16 16" aria-hidden="true">
            <rect x="1.5" y="3" width="13" height="10" fill="none" stroke="#27b9dd" stroke-width="1.3"/>
            <path d="M1.5 3.5L8 9l6.5-5.5" fill="none" stroke="#27b9dd" stroke-width="1.3"/>
          </svg>
          owenhalburyroofing@tindlemail.com
        </p>
      </div>
    </div>
  </section>

  <section class="card card--back" aria-label="Business card back">
    <div class="band">
      <div class="services">
        <p class="services__item">Residential &amp; Commercial</p>
        <p class="services__item">Re-roof &amp; New Construction</p>
        <p class="services__item">Fully Insured</p>
      </div>
    </div>
  </section>

</main>
</body>
</html>
```